Small Box Design - For launch into retail market

We need artwork for small boxes that we are going to be using for the retail market. I will upload the type of box we are going to be using. The example we are uploading is of a different company that sells the same products. We would like our Logo on the box as as our web address (www.kestonbarlow.example). The rest is up to you. Please contact with any questions.

Target Market(s)

Distributors, Retailers of Fasteners

Industry/Entity Type

Manufacture

Colors
0355a3
3176b5
fbee3f
fbf289

Requirements
Must have
• Our logo, our web address www.kestonbarlow.example
• Somewhere on the box Washers . Stampings . Assemblies . Bearings (most likely below our logo somewhere)
Nice to have
• Blue is our corporate colour, but it's not essential. You can suggest any colours and we will consider.

```html
<!DOCTYPE html>
<html lang="en">
<head>
<meta charset="utf-8">
<title>Keston Barlow Retail Carton Dieline</title>
<link href="https://fonts.googleapis.com/css2?family=Montserrat:wght@400;600;700&display=swap" rel="stylesheet">
<style>
  :root {
    --page: #d8d9da;
    --brand-blue: #0455b7;
    --carton-grey: #6e6e70;
    --fold: rgba(255,255,255,0.75);
    --ink-light: #ffffff;
    --accent: #e29a2e;
    --pattern-tint: rgba(255,255,255,0.05);
  }
  html, body { margin: 0; padding: 0; overflow: hidden; }
  body { width: 972px; height: 1200px; background: var(--page); }
  .dieline { display: block; width: 972px; height: 1200px; }
  .panel-blue { fill: var(--brand-blue); }
  .panel-grey { fill: var(--carton-grey); }
  .fold-line { fill: none; stroke: var(--fold); stroke-width: 1; }
  .pattern-wash { fill: var(--pattern-tint); }
  .brand-name { font-family: "Montserrat", sans-serif; font-weight: 600; fill: var(--ink-light); font-size: 28px; }
  .brand-sub { font-family: "Montserrat", sans-serif; font-weight: 400; fill: var(--ink-light); font-size: 12px; letter-spacing: 1px; text-anchor: middle; }
  .brand-dot { fill: var(--accent); }
  .web-address { font-family: "Montserrat", sans-serif; font-weight: 700; fill: var(--ink-light); font-size: 13px; letter-spacing: 2.6px; text-anchor: middle; }
  .product-line { font-family: "Montserrat", sans-serif; font-weight: 600; fill: var(--ink-light); font-size: 8.5px; letter-spacing: 0.8px; text-anchor: middle; }
  .about-head { font-family: "Montserrat", sans-serif; font-weight: 600; fill: var(--ink-light); font-size: 8.5px; text-anchor: middle; }
  .about-copy { font-family: "Montserrat", sans-serif; font-weight: 400; fill: var(--ink-light); font-size: 8.5px; text-anchor: middle; }
  .carton-no { font-family: "Montserrat", sans-serif; font-weight: 700; fill: var(--ink-light); text-anchor: middle; }
  .recycle-ring { fill: none; stroke: var(--ink-light); stroke-width: 9; }
  .recycle-head { fill: var(--ink-light); }
</style>
</head>
<body>
<svg class="dieline" viewBox="0 0 1215 1500" xmlns="http://www.w3.org/2000/svg">
  <defs>
    <clipPath id="carton-outline">
      <path d="M440,103 H835 V112 C935,118 995,175 995,255 V285 Q995,320 960,320 H835 V412 H930 L940,400 H1003 L1013,412 H1110 V605 H1125 V930 H835 V1095 H1125 V1322 H152 V1095 H440 V930 H152 V605 H163 V412 H262 L272,400 H335 L345,412 H440 V320 H320 Q285,320 285,285 V255 C285,175 345,118 440,112 Z"/>
    </clipPath>
  </defs>

  <!-- top tuck flap -->
  <path class="panel-grey" d="M440,103 H835 V112 C935,118 995,175 995,255 V285 Q995,320 960,320 H320 Q285,320 285,285 V255 C285,175 345,118 440,112 Z"/>
  <!-- centre column -->
  <rect class="panel-blue" x="440" y="320" width="395" height="290"/>
  <rect class="panel-grey" x="440" y="930" width="395" height="165"/>
  <!-- side dust flaps -->
  <path class="panel-blue" d="M163,412 H262 L272,400 H335 L345,412 H440 V608 H163 Z"/>
  <path class="panel-blue" d="M835,412 H930 L940,400 H1003 L1013,412 H1110 V608 H835 Z"/>
  <!-- main wrap row -->
  <rect class="panel-blue" x="152" y="605" width="973" height="127"/>
  <rect class="panel-grey" x="152" y="732" width="973" height="198"/>
  <!-- bottom strip -->
  <rect class="panel-grey" x="152" y="1095" width="973" height="95"/>
  <rect class="panel-blue" x="152" y="1190" width="973" height="132"/>

  <!-- faint washer pattern across the whole carton -->
  <rect class="pattern-wash" x="152" y="103" width="973" height="1219" clip-path="url(#carton-outline)" role="img" aria-label="Faint repeating pattern of stamped washers"/>

  <!-- fold and cut guides -->
  <path class="fold-line" d="M448,112 H828 V320 M448,112 V320 M448,320 H828"/>
  <path class="fold-line" d="M290,300 V260 C290,180 350,122 448,118 M990,300 V260 C990,180 930,122 828,118 M290,300 Q292,316 320,316 H448 M990,300 Q988,316 960,316 H828"/>
  <rect class="fold-line" x="175" y="420" width="260" height="188"/>
  <rect class="fold-line" x="840" y="420" width="262" height="188"/>
  <path class="fold-line" d="M448,320 V1312 M828,320 V1312"/>
  <path class="fold-line" d="M160,608 H1115 M160,817 H1115 M160,608 V920 H448 M1115,608 V920 H828"/>
  <rect class="fold-line" x="160" y="1105" width="955" height="207"/>

  <!-- upside-down top panel: logo and about copy -->
  <g transform="rotate(180 638 378)">
    <circle class="brand-dot" cx="530" cy="370" r="8"/>
    <text class="brand-name" x="546" y="380" textLength="209" lengthAdjust="spacingAndGlyphs">Keston Barlow</text>
    <text class="brand-sub" x="650" y="399">LIMITED</text>
  </g>
  <g transform="rotate(180 638 275)">
    <text class="web-address" x="638" y="248">www.kestonbarlow.example</text>
    <text class="about-head" x="638" y="265">KESTON BARLOW IS NOT JUST ANOTHER WASHER MANUFACTURER</text>
    <text class="about-copy" x="638" y="277">Keston Barlow is recognized as a pioneer in the design of innovative stamping</text>
    <text class="about-copy" x="638" y="289">equipment. We have made our name through exceptional quality,</text>
    <text class="about-copy" x="638" y="301">our astute knowledge, and an enthusiastic desire to drive technology.</text>
  </g>

  <!-- front faces -->
  <g>
    <circle class="brand-dot" cx="196" cy="675" r="8"/>
    <text class="brand-name" x="212" y="685" textLength="209" lengthAdjust="spacingAndGlyphs">Keston Barlow</text>
    <text class="brand-sub" x="316" y="706">LIMITED</text>
    <text class="web-address" x="304" y="750">www.kestonbarlow.example</text>
    <text class="product-line" x="304" y="775">Washers . Stampings . Assemblies . Bearings</text>

    <circle class="brand-dot" cx="530" cy="675" r="8"/>
    <text class="brand-name" x="546" y="685" textLength="209" lengthAdjust="spacingAndGlyphs">Keston Barlow</text>
    <text class="brand-sub" x="650" y="706">LIMITED</text>
    <text class="web-address" x="638" y="750">www.kestonbarlow.example</text>
    <text class="product-line" x="638" y="775">Washers . Stampings . Assemblies . Bearings</text>

    <circle class="brand-dot" cx="863" cy="675" r="8"/>
    <text class="brand-name" x="879" y="685" textLength="209" lengthAdjust="spacingAndGlyphs">Keston Barlow</text>
    <text class="brand-sub" x="983" y="706">LIMITED</text>
    <text class="web-address" x="971" y="750">www.kestonbarlow.example</text>
    <text class="product-line" x="971" y="775">Washers . Stampings . Assemblies . Bearings</text>
  </g>

  <!-- recycle mark and carton number -->
  <g>
    <circle class="recycle-ring" cx="655" cy="967" r="32" stroke-dasharray="52 15"/>
    <polygon class="recycle-head" points="682,938 690,958 668,956"/>
    <polygon class="recycle-head" points="648,1005 628,992 648,984"/>
    <polygon class="recycle-head" points="625,948 640,933 646,952"/>
    <text class="carton-no" transform="translate(572 962) rotate(90)" font-size="28">4</text>
    <text class="carton-no" transform="translate(598 962) rotate(90)" font-size="5">CARTON</text>
  </g>

  <!-- upside-down bottom strip: about copy and logo -->
  <g transform="rotate(180 638 1147)">
    <text class="web-address" x="638" y="1120">www.kestonbarlow.example</text>
    <text class="about-head" x="638" y="1137">KESTON BARLOW IS NOT JUST ANOTHER WASHER MANUFACTURER</text>
    <text class="about-copy" x="638" y="1149">Keston Barlow is recognized as a pioneer in the design of innovative stamping</text>
    <text class="about-copy" x="638" y="1161">equipment. We have made our name through exceptional quality,</text>
    <text class="about-copy" x="638" y="1173">our astute knowledge, and an enthusiastic desire to drive technology.</text>
  </g>
  <g transform="rotate(180 638 1245)">
    <circle class="brand-dot" cx="530" cy="1237" r="8"/>
    <text class="brand-name" x="546" y="1247" textLength="209" lengthAdjust="spacingAndGlyphs">Keston Barlow</text>
    <text class="brand-sub" x="650" y="1266">LIMITED</text>
  </g>
</svg>
</body>
</html>
```